my catalog design project for KTR tradeshow

We need a catalog design for our ranch equipment manufacturing company. The final design should communicate low cost alternative without compromising quality.
We need all the main product lines show cased in catalog including gates, panels, feeders, cattle squeezes, horse stalls, dog kennels, tractor attachments
The layout, design and colors can reflect the design of the website:

We just need a basic product catalog that uses a similar layout, design, and colors as our website: hollowcrestfabricating.com

Catalog should be approximately 6-10 pages long 8.5"x11" first page cover, next inside page company info, then product pages with item picture and description as in the website. For sample submissions, i'd like to see cover page, inside page and a product page.

FOR THE INITIAL ENTRIES, I'm expecting to see
- the cover page,
- inside company info page
- and one product page.

Target Market(s)

Chain Store buyers

Industry/Entity Type

Agriculture

Requirements
Must have
• All the product info details of main products

```html
<!DOCTYPE html>
<html lang="en">
<head>
<meta charset="utf-8">
<title>Hollowcrest Fabricating – Gates</title>
<link rel="stylesheet" href="https://fonts.googleapis.com/css2?family=Montserrat:wght@400;500;600;700&display=swap">
<style>
  :root {
    --brand-red: #7b1416;
    --accent-red: #8e1b1d;
    --ink: #1d1d1b;
    --band-grey: #e1e1e1;
    --row-grey: #e3e3e3;
    --row-line: #ffffff;
    --paper: #ffffff;
    --gate-tone: #9a5a4e;
    --gate-tone-light: #c79a90;
  }
  * { box-sizing: border-box; margin: 0; padding: 0; }
  html, body { width: 928px; height: 1200px; overflow: hidden; background: var(--paper); }
  body { font-family: "Montserrat", Arial, sans-serif; color: var(--ink); }
  .page { position: relative; width: 928px; height: 1200px; background: var(--paper); overflow: hidden; }

  .brand-name {
    position: absolute; right: 76px; top: 64px;
    font-weight: 700; font-size: 30px; letter-spacing: 0.5px;
    color: var(--ink); text-align: right; line-height: 1.1;
  }
  .brand-name span { display: block; }

  .top-strip { position: absolute; left: 179px; top: 164px; width: 749px; height: 18px; background: var(--band-grey); }
  .section-band {
    position: absolute; left: 179px; top: 186px; width: 749px; height: 79px;
    background: var(--brand-red); display: flex; align-items: center; padding-left: 34px;
  }
  .section-title {
    color: #fff; font-weight: 700; font-size: 28px; letter-spacing: 1px;
    display: flex; align-items: center; gap: 10px;
  }
  .section-title svg { width: 12px; height: 14px; }

  .product-image {
    position: absolute; left: 200px; top: 383px; width: 643px; height: 207px;
    background: linear-gradient(180deg, var(--gate-tone-light), var(--gate-tone));
    opacity: 0.55;
  }

  .product-name {
    position: absolute; left: 200px; top: 670px;
    font-size: 18px; font-weight: 600; color: var(--accent-red);
  }

  .spec-table { position: absolute; left: 179px; top: 778px; width: 696px; }
  .spec-head {
    display: flex; justify-content: space-between; padding: 0 32px 0 7px;
    font-size: 17px; font-weight: 600; height: 40px; align-items: flex-start;
    border-bottom: 8px solid var(--brand-red);
  }
  .spec-row {
    display: flex; background: var(--row-grey);
    border-bottom: 1.5px solid var(--row-line); font-size: 15px; font-weight: 500;
  }
  .spec-row .desc { width: 575px; padding-left: 15px; border-right: 1.5px solid var(--row-line); display: flex; align-items: center; }
  .spec-row .weight { flex: 1; display: flex; align-items: center; justify-content: center; }
  .spec-row.intro { height: 77px; }
  .spec-row.intro .desc { align-items: flex-start; padding-top: 11px; line-height: 1.7; }
  .spec-row.intro .weight { align-items: flex-start; padding-top: 11px; color: #444; font-weight: 400; }
  .spec-row.item { height: 31px; }
  .spec-row.item .desc { padding-left: 19px; }
</style>
</head>
<body>
<div class="page">
  <div class="brand-name"><span>HOLLOWCREST</span><span>FABRICATING</span></div>

  <div class="top-strip"></div>
  <div class="section-band">
    <h1 class="section-title">
      <svg viewBox="0 0 12 14"><polygon points="0,0 12,7 0,14" fill="#fff"/></svg>
      GATES
    </h1>
  </div>

  <div class="product-image" role="img" aria-label="Photo of a red five-rail medium duty steel gate with hinges and chain latch"></div>

  <h2 class="product-name">Medium Duty Gates</h2>

  <div class="spec-table">
    <div class="spec-head"><span>DESCRIPTION</span><span>WEIGHT Es.</span></div>
    <div class="spec-row intro">
      <div class="desc">1 5/8" x 15 ga. verticals 18 ga.<br>Internal Pipe, 48" Tall, 1" Bolt Hinge, 39" Chain Latch</div>
      <div class="weight">In Pounds</div>
    </div>
    <div class="spec-row item"><div class="desc">4' Gate, Five Rail</div><div class="weight">32</div></div>
    <div class="spec-row item"><div class="desc">6' Gate, Five Rail</div><div class="weight">43</div></div>
    <div class="spec-row item"><div class="desc">8' Gate, Five Rail</div><div class="weight">52</div></div>
    <div class="spec-row item"><div class="desc">10' Gate, Five Rail</div><div class="weight">61</div></div>
    <div class="spec-row item"><div class="desc">12' Gate, Five Rail</div><div class="weight">69</div></div>
    <div class="spec-row item"><div class="desc">14' Gate, Five Rail</div><div class="weight">82</div></div>
    <div class="spec-row item"><div class="desc">16' Gate, Five Rail</div><div class="weight">91</div></div>
  </div>
</div>
</body>
</html>
```